Downtown Walking Map Layout (Map Provided)

My company is in need of a refreshed layout of our downtown walking map. We have an illustrated map of downtown that we want to use, listings completed, and content with photos. We have edited the map so many times that you can now see design elements from each of them and we need a new fresh design. We can send over an indesign file of the attached PDF and all listings in a spreadsheet if that would be helpful. We can also provide access to our photography assets for you to use.
Updates

Need extra days to review

Target Market(s)

Downtown Patrons

Industry/Entity Type

Tourism

Font styles to use
Other font styles liked:
• Domine Display, Monterrat (Light to bold versions)

Colors

Designer to choose colors to be used in the design.

Requirements
Must have
• The illustrated map we provide, all listings and categories, must be accurate size and fold design, the events content provided. Branding must follow our brand guidebook that is provided.
Should not have
• Brand elements that are not or do not compliment our brand.

```html
<!DOCTYPE html>
<html lang="en">
<head>
<meta charset="utf-8">
<title>A Guide to Downtown Alderport – Walking Map Brochure</title>
<link rel="stylesheet" href="https://fonts.googleapis.com/css2?family=DM+Serif+Display&family=Montserrat:ital,wght@0,300;0,400;0,600;1,400&display=swap">
<style>
:root{
  --backdrop:#d4d4d4;
  --paper:#ffffff;
  --ink:#3c3c3c;
  --tan:#cdb089;
  --coral:#f2927a;
  --coral-deep:#ee7676;
  --mint:#b9d9c5;
  --mauve:#a3898b;
  --teal:#2f6e78;
  --pink-soft:#e9a2bb;
  --sun:#f2c84f;
  --olive-brown:#8d7f5c;
  --slate-mist:#9fb1b9;
  --charcoal-green:#55615c;
  --violet:#5b4a9c;
  --rose:#e37189;
  --amber:#f1aa3a;
  --blue:#2b5aa6;
  --red:#e05b6b;
  --pine:#2f6c69;
  --mustard:#c9a45c;
  --moss:#a9ad4b;
  --stone:#a19b91;
  --periwinkle:#a4acc2;
  --blush:#e9a3aa;
  --leaf:#5b9b70;
  --lavender:#7e79b1;
  --rust:#d9683a;
  --butter:#f5d870;
}
*{box-sizing:border-box;margin:0;padding:0}
html,body{width:1200px;height:1010px;overflow:hidden;background:var(--backdrop)}
body{font-family:"Montserrat",sans-serif;color:var(--ink)}
.brochure{position:absolute;left:150px;top:55px;width:900px;height:900px;background:var(--paper);box-shadow:0 2px 6px rgba(0,0,0,.18)}
.half{position:absolute;left:0;width:900px;height:450px}
.half--inside{top:0;transform:rotate(180deg)}
.half--outside{top:450px}
.tile-grid{position:absolute;display:grid;grid-template-columns:repeat(8,1fr);grid-template-rows:repeat(4,1fr);gap:6px;width:576px;height:411px}
.half--outside .tile-grid{left:10px;top:10px}
.half--inside .tile-grid{left:314px;top:29px}
.tile{position:relative;overflow:hidden;padding:6px 5px;color:#fff}
.photo{padding:0}
.tile h3,.headline{font-family:"DM Serif Display",serif;font-weight:400;line-height:1;letter-spacing:-.2px}
.tile h3{font-size:11.5px;margin-bottom:4px}
.tile p{font-size:6px;line-height:1.35}
.tile .when{display:block;margin-top:3px;text-transform:uppercase;font-size:5.4px;letter-spacing:.2px;line-height:1.3}
.tile--events h3{font-size:30px;margin-top:6px}
.photo-label{position:absolute;left:8px;top:8px;font-family:"DM Serif Display",serif;font-size:24px;color:#fff;line-height:.95}
.photo-label--band{left:0;top:0;right:0;background:var(--paper);color:var(--ink);padding:4px 8px 6px}
.cover{position:absolute;left:604px;top:10px;width:286px;height:430px;display:flex;flex-direction:column}
.cover .headline{color:var(--tan);font-size:27px;line-height:1;padding:6px 4px 12px}
.cover .photo{flex:1}
.cover-url{background:var(--butter);color:#fff;font-size:8px;text-align:center;padding:7px 0;letter-spacing:.4px}
.welcome{position:absolute;left:12px;top:29px;width:280px;height:411px;padding:6px 10px;display:flex;flex-direction:column}
.welcome .headline{color:var(--tan);font-size:32px;margin-bottom:10px}
.welcome p{font-size:6.6px;line-height:1.5;margin-bottom:7px}
.welcome .signoff{font-style:italic;font-size:8px;margin-top:4px}
.wordmark{margin-top:auto;display:flex;align-items:center;gap:8px;font-size:10px;font-weight:600;letter-spacing:.3px}
.wordmark .mark{width:22px;height:22px;border:1px solid var(--ink)}
</style>
</head>
<body>
<main class="brochure">

  <section class="half half--inside">
    <article class="welcome">
      <h2 class="headline">hello.</h2>
      <p>Welcome to downtown Alderport, where our historic streets are full of local shops, friendly faces and flavor. Whether you are here for an afternoon or a week, we hope this guide helps you find your way.</p>
      <p>Stroll the main corridor to discover galleries, boutiques, bakeries and cafés owned by your neighbors. Many of our storefronts have served the community for generations, and new makers arrive every season.</p>
      <p>Use the map inside to plan a walking route, then stop in to say hello. Our merchants love sharing stories about the town and its history.</p>
      <p>Thank you for choosing to shop, dine and explore locally. Every visit helps keep our downtown vibrant.</p>
      <p class="signoff">Your friends downtown</p>
      <div class="wordmark"><span class="mark"></span><span>City of Alderport</span></div>
    </article>

    <div class="tile-grid">
      <div class="tile photo" style="grid-column:1/3;grid-row:1/3;background:linear-gradient(#c9d4dc,#7d7364)" role="img" aria-label="Photo of a tree-lined downtown street with a lamppost">
        <span class="photo-label photo-label--band">second<br>street.</span>
      </div>
      <div class="tile photo" style="grid-column:3/5;grid-row:1;background:linear-gradient(#8fb3cf,#4d6a86)" role="img" aria-label="Photo of the library building reflected in water">
        <span class="photo-label">library.</span>
      </div>
      <div class="tile" style="grid-column:5;grid-row:1;background:var(--pine)"><p>A welcoming space with books, free wifi and events for all ages.</p></div>
      <div class="tile" style="grid-column:6;grid-row:1;background:var(--red)"></div>
      <div class="tile" style="grid-column:7/9;grid-row:1;background:var(--blue)">
        <h3>need a bite to eat?</h3>
        <p>From cozy cafés and bakeries to pubs and fine dining, downtown has a flavor for every appetite and budget.</p>
      </div>

      <div class="tile" style="grid-column:3;grid-row:2;background:var(--moss)"></div>
      <div class="tile" style="grid-column:4;grid-row:2;background:var(--mustard)"></div>
      <div class="tile photo" style="grid-column:5/9;grid-row:2;background:linear-gradient(90deg,#b0534a,#d9b49a,#6b4a3a)" role="img" aria-label="Photo of friends sharing a meal at a downtown restaurant">
        <span class="photo-label">eat.</span>
      </div>

      <div class="tile" style="grid-column:1/3;grid-row:3;background:var(--stone)"><p>Historic buildings line this walkable stretch, home to antique dealers, galleries and local favorites.</p></div>
      <div class="tile photo" style="grid-column:3/5;grid-row:3/5;background:linear-gradient(#c58b5a,#7a4e36)" role="img" aria-label="Photo of a shopkeeper holding a basket of local goods">
        <span class="photo-label">shop.</span>
      </div>
      <div class="tile" style="grid-column:5/7;grid-row:3;background:var(--stone)"><h3>alderport<br>playhouse.</h3></div>
      <div class="tile photo" style="grid-column:7/9;grid-row:3;background:linear-gradient(#8a8678,#5a5448)" role="img" aria-label="Photo of the historic playhouse lobby"></div>

      <div class="tile" style="grid-column:1;grid-row:4;background:var(--rust)"></div>
      <div class="tile" style="grid-column:2;grid-row:4;background:var(--lavender)"></div>
      <div class="tile" style="grid-column:5/7;grid-row:4;background:var(--leaf)"><p>Our merchants offer a wide variety of gifts, clothing, home goods and treasures you won't find anywhere else.</p></div>
      <div class="tile" style="grid-column:7;grid-row:4;background:var(--blush)"><p>Find a gift for someone special today.</p></div>
      <div class="tile" style="grid-column:8;grid-row:4;background:var(--periwinkle)"></div>
    </div>
  </section>

  <section class="half half--outside">
    <div class="tile-grid">
      <div class="tile photo" style="grid-column:1;grid-row:1;background:linear-gradient(#9cc0dd,#b68a6e)" role="img" aria-label="Photo of a brick downtown building"></div>
      <div class="tile" style="grid-column:2;grid-row:1;background:var(--coral)"><h3>moonlight madness.</h3><p>Shops stay open late with sales and specials.<span class="when">August</span></p></div>
      <div class="tile photo" style="grid-column:3/5;grid-row:1;background:linear-gradient(90deg,#5a4a4a,#a44a4a,#6a6560)" role="img" aria-label="Photo of costumed children trick-or-treating"></div>
      <div class="tile" style="grid-column:5;grid-row:1;background:var(--mint)"><h3>downtown trick or treat.</h3><p>Costumed kids visit shops.<span class="when">October</span></p></div>
      <div class="tile" style="grid-column:6;grid-row:1;background:var(--mauve)"><h3>cork &amp; brew tour.</h3><p>A guided walking tour of local wine and beer.<span class="when">June</span></p></div>
      <div class="tile photo" style="grid-column:7;grid-row:1;background:linear-gradient(#9a8a7a,#5a5048)" role="img" aria-label="Photo of friends toasting on a tour"></div>
      <div class="tile photo" style="grid-column:8;grid-row:1;background:linear-gradient(#b7a48a,#6a4e3c)" role="img" aria-label="Photo of a storefront entrance"></div>

      <div class="tile" style="grid-column:1;grid-row:2;background:var(--teal)"><h3>sip + shop.</h3><p>Shops stay open late with drink samples.<span class="when">Second Friday of each month</span></p></div>
      <div class="tile photo" style="grid-column:2;grid-row:2;background:linear-gradient(#d8c8b4,#8a7664)" role="img" aria-label="Photo of shoppers in a boutique"></div>
      <div class="tile" style="grid-column:3;grid-row:2;background:var(--pink-soft)"><h3>light parade.</h3><p>Lighted parade with holiday cheer.<span class="when">December</span></p></div>
      <div class="tile photo" style="grid-column:4/6;grid-row:2;background:linear-gradient(90deg,#c9d3da,#b83a3a,#2a2a3a)" role="img" aria-label="Photo of a parade banner carried down the street"></div>
      <div class="tile" style="grid-column:6;grid-row:2;background:var(--sun)"><h3>june dairy parade.</h3><p>An old-fashioned parade downtown.<span class="when">June</span></p></div>
      <div class="tile" style="grid-column:7/9;grid-row:2;background:var(--olive-brown)"><h3>art walk.</h3><p>Galleries and shops showcase local artists.<span class="when">Third Saturday of each month</span></p></div>

      <div class="tile tile--events" style="grid-column:1/3;grid-row:3;background:var(--coral)"><h3>events.</h3></div>
      <div class="tile photo" style="grid-column:3;grid-row:3;background:linear-gradient(#9a6a5a,#4a3a34)" role="img" aria-label="Photo of a vendor at the market"></div>
      <div class="tile" style="grid-column:4;grid-row:3;background:var(--slate-mist)"><h3>alderport farmers market.</h3><p>Local produce, crafts and food.<span class="when">June – September</span></p></div>
      <div class="tile photo" style="grid-column:5/7;grid-row:3;background:linear-gradient(90deg,#4a4a46,#a89a88,#6a7a88)" role="img" aria-label="Photo of two neighbors chatting over coffee"></div>
      <div class="tile" style="grid-column:7/9;grid-row:3;background:var(--coral-deep)"><h3>mornings on main street.</h3><p>Join the chamber for coffee and conversation.<span class="when">Second Tuesday of each month</span></p></div>

      <div class="tile photo" style="grid-column:1;grid-row:4;background:linear-gradient(#a88a70,#5a4438)" role="img" aria-label="Photo of shoppers outside a store"></div>
      <div class="tile" style="grid-column:2;grid-row:4;background:var(--charcoal-green)"><h3>small business saturday.</h3><p>Specials and family events.<span class="when">Saturday after Thanksgiving</span></p></div>
      <div class="tile photo" style="grid-column:3/5;grid-row:4;background:linear-gradient(90deg,#7a8a6a,#e0d8d0,#3a3a40)" role="img" aria-label="Photo of dancers in traditional costume"></div>
      <div class="tile" style="grid-column:5/7;grid-row:4;background:var(--violet)"><h3>oktoberfest.</h3><p>Celebrate with music, dancing and drinks on the plaza.<span class="when">September</span></p></div>
      <div class="tile" style="grid-column:7;grid-row:4;background:var(--rose)"></div>
      <div class="tile" style="grid-column:8;grid-row:4;background:var(--amber)"></div>
    </div>

    <aside class="cover">
      <h1 class="headline">a guide to<br>downtown<br>alderport.</h1>
      <div class="photo" role="img" aria-label="Photo of a downtown storefront with a restaurant awning and lamppost" style="background:linear-gradient(#eef0f0 0%,#b8a890 45%,#5e5a52 100%)"></div>
      <div class="cover-url">www.goalderport.com</div>
    </aside>
  </section>

</main>
</body>
</html>
```